Data Analysis new tech startup

Design a simple / modern website (one page, one language) with a tech touch, based on the words prediction and/or IoT (Internet of Things).

VORELM IoT is dedicated for Data Analysis of IoT or M2M (Machine to Machine) projects.

The website should follow the colors of the logo (see images)

The web site should look like this example: https://bastuvo-analytics.example/en/ with less human pictures and ALL the text content should be configurable for later change.

The website will be published on a php web server.

Target Market(s)

Business professionals

Industry/Entity Type

Data Science

Coding

Coded - Design and coding required

Number of Pages Required

1 page

Colors

Designer to choose colors to be used in the design.

Requirements
Must have
• Follow example site guidelines (https://bastuvo-analytics.example/en/)
• Follow logo colors
• Fun and startup look and feel
• ALL TEXT SHOULD BE CONFIGURABLE
• Clients carrousel with colored hovering
Nice to have
• Configurable photo carrousel at the top (after menu)
Should not have
• Too many human photos, just a few.

```html
<!DOCTYPE html>
<html lang="en">
<head>
<meta charset="utf-8">
<title>VORELM IoT — Data Analysis for IoT &amp; M2M</title>
<link href="https://fonts.googleapis.com/css2?family=Poppins:wght@300;400;500;600;700&display=swap" rel="stylesheet">
<style>
:root{
  --purple:#6b22d8;
  --violet:#8a2be2;
  --magenta:#e0157f;
  --pink:#ff3d7f;
  --navy:#1d1f3b;
  --ink:#2a2a3a;
  --muted:#7a7a8c;
  --light:#f4f4f6;
  --line:#e6e6ec;
  --white:#ffffff;
  --grad:linear-gradient(90deg,var(--magenta),var(--purple));
}
*{box-sizing:border-box;margin:0;padding:0}
html,body{width:1200px;height:5263px;overflow:hidden}
body{position:relative;font-family:'Poppins',sans-serif;color:var(--ink);background:var(--white)}
.abs{position:absolute}
.section-title{position:absolute;left:0;width:1200px;text-align:center;font-size:27px;font-weight:600;color:var(--navy)}

/* header */
.site-header{left:0;top:0;width:1200px;height:77px;background:var(--white)}
.brand{left:182px;top:20px;display:flex;align-items:center;gap:10px;font-size:27px;font-weight:700;color:var(--navy);letter-spacing:.5px}
.brand-mark{width:22px;height:22px;background:var(--magenta);border-radius:3px}
.main-nav{left:527px;top:30px;display:flex;gap:38px;font-size:11px;font-weight:500;color:var(--ink);letter-spacing:.4px}
.main-nav .active{color:var(--magenta);border-bottom:2px solid var(--magenta);padding-bottom:4px}

/* hero */
.hero{left:0;top:77px;width:1200px;height:449px;background:linear-gradient(100deg,#ff2a78 0%,#d11f8f 30%,#7a2ae6 70%,#4b3fd8 100%);overflow:hidden}
.hero-photo{right:0;top:0;width:760px;height:449px;background:linear-gradient(100deg,rgba(120,40,220,0) 0%,rgba(70,60,190,.55) 45%,rgba(40,50,120,.7) 100%)}
.hero-text{left:182px;top:130px;color:var(--white)}
.hero-kicker{font-size:14px;font-weight:500;letter-spacing:1px}
.hero-title{font-size:34px;font-weight:700;line-height:1.15;margin-top:10px;width:340px}
.hero-sub{font-size:13px;margin-top:18px;opacity:.9}

/* methodology */
.method-intro{left:330px;top:660px;width:540px;text-align:center;font-size:12px;line-height:1.75;color:var(--muted)}
.method-item{width:300px;text-align:center}
.method-item svg{display:block;margin:0 auto 10px}
.method-item h3{font-size:16px;font-weight:500;color:var(--magenta);margin-bottom:10px}
.method-item p{font-size:11.5px;line-height:1.7;color:var(--muted)}

/* offering */
.offering{left:0;top:1298px;width:1200px;height:1544px;background:var(--light)}
.offer-intro{left:182px;top:1446px;width:360px}
.offer-intro h3{font-size:16px;font-weight:500;line-height:1.5;color:var(--navy)}
.offer-intro p{font-size:11.5px;line-height:1.7;color:var(--muted);margin-top:8px}
.illustration{border-radius:16px}
.offer-card{width:408px;background:var(--white);box-shadow:0 12px 30px rgba(60,40,120,.12);padding:36px 40px 30px;overflow:hidden}
.offer-card .blob{position:absolute;right:-10px;top:-10px}
.offer-card h4{font-size:15px;font-weight:600;line-height:1.35;background:var(--grad);-webkit-background-clip:text;background-clip:text;color:transparent;width:170px}
.offer-card hr{border:0;border-top:1px solid var(--line);margin:20px 0 22px}
.offer-group{margin-bottom:22px}
.offer-group h5{font-size:12px;font-weight:600;color:var(--ink);margin-bottom:6px}
.offer-group li{list-style:none;font-size:11px;color:var(--muted);line-height:1.9;padding-left:16px;position:relative}
.offer-group li::before{content:"";position:absolute;left:2px;top:8px;width:6px;height:6px;border-radius:50%;background:var(--purple)}

/* life */
.tile{overflow:hidden}
.clients-tile{background:linear-gradient(135deg,var(--purple),var(--magenta) 90%);color:var(--white);padding:42px 36px}
.clients-tile small{display:block;font-size:20px;font-weight:300}
.clients-tile strong{font-size:44px;font-weight:700;line-height:1.1}
.photo{background:linear-gradient(135deg,#5b6478,#2c3140)}
.quote-tile{background:var(--white);box-shadow:0 10px 30px rgba(0,0,0,.08);padding:48px 34px}
.quote-mark{font-size:90px;line-height:.7;color:var(--magenta);font-weight:700}
.quote-tile p{font-size:11.5px;line-height:1.7;color:var(--muted);margin-top:22px}
.quote-tile .who{font-size:11px;color:var(--ink);margin-top:18px}
.quote-tile .who span{color:var(--magenta)}
.stats-tile{background:linear-gradient(135deg,var(--magenta),var(--purple));color:var(--white);display:grid;grid-template-columns:1fr 1fr;padding:30px 36px;row-gap:20px}
.stats-tile b{display:block;font-size:24px;font-weight:600}
.stats-tile span{font-size:11px;opacity:.85}

/* career */
.career-photo{left:0;top:3888px;width:1200px;height:428px;background:linear-gradient(120deg,#cdbfae,#8f8576 50%,#e9e4dc)}
.join-card{left:326px;top:4113px;width:548px;height:273px;background:linear-gradient(120deg,#4a49e0,var(--purple) 60%,#8b2be0);color:var(--white);text-align:center;padding:42px 50px;box-shadow:0 18px 40px rgba(70,40,180,.3)}
.join-card h3{font-size:23px;font-weight:600}
.join-card p{font-size:12px;line-height:1.7;margin-top:14px;opacity:.92}
.join-card a{display:inline-block;margin-top:22px;background:var(--white);color:var(--purple);font-size:12px;font-weight:500;padding:9px 34px;border-radius:22px;text-decoration:none}

/* trust */
.trust-row{left:250px;top:4540px;width:700px;display:flex;justify-content:space-between;align-items:center}
.trust-name{display:flex;align-items:center;gap:8px;font-size:16px;font-weight:600;color:#6c6c78;letter-spacing:.5px}
.trust-name i{width:12px;height:12px;border-radius:50%;background:#9a9aa6}
.trust-arrow{top:4544px;font-size:22px;color:#c4c4cc}

/* contact */
.contact{left:0;top:4649px;width:1200px;height:228px;background:var(--light)}
.contact-pill{top:4762px;height:52px;background:var(--white);border-radius:26px;box-shadow:0 6px 18px rgba(0,0,0,.07);display:flex;align-items:center;justify-content:center;gap:14px;font-size:13px;color:var(--ink)}

/* footer */
.site-footer{left:0;top:4877px;width:1200px;height:386px;background:linear-gradient(90deg,#e0157f,#c8177f 50%,#e0157f);color:var(--white)}
.office{top:4948px;width:130px;font-size:11px;line-height:1.6}
.office svg{display:block;margin-bottom:8px}
.office b{display:block;font-weight:600;font-size:12px;margin-bottom:3px}
.footer-rule{left:182px;top:5130px;width:836px;border-top:1px solid rgba(255,255,255,.35)}
.footer-nav{left:182px;top:5164px;display:flex;gap:42px;font-size:10px;font-weight:500;letter-spacing:.4px}
.copyright{left:182px;top:5196px;font-size:9.5px;opacity:.85}
.socials{left:940px;top:5164px;display:flex;gap:10px}
.socials i{width:12px;height:12px;border-radius:50%;background:var(--white);opacity:.9}
</style>
</head>
<body>

<header class="abs site-header">
  <div class="abs brand"><span class="brand-mark"></span>VORELM IoT</div>
  <nav class="abs main-nav">
    <span class="active">OUR METHODOLOGY</span><span>OUR OFFERING</span><span>CAREERS</span><span>LIFE AT VORELM</span><span>CONTACT</span>
  </nav>
</header>

<section class="abs hero">
  <div class="abs hero-photo" role="img" aria-label="Hands typing on a keyboard with a glowing data overlay"></div>
  <div class="abs hero-text">
    <div class="hero-kicker">VORELM IOT</div>
    <h1 class="hero-title">Lorem ipsum dolor amet adipisclot</h1>
    <p class="hero-sub">Commodo pharetra dolor</p>
  </div>
</section>

<h2 class="section-title" style="top:600px">Our Methodology</h2>
<p class="abs method-intro">Pellentesque imperdiet ut lacus tincidunt. Maecenas in fringilla ipsum. Phasellus ac magna nec fusce dictum volutpat. Morbi in libero molestie, orci ut vestibulum auctor, quam nunc consectetur felis. Nulla feugiat porttitor dui vel tincidunt. Maecenas et fringilla lorem. Phasellus ac magna leo.</p>

<div class="abs method-item" style="left:232px;top:780px">
  <svg width="48" height="48" viewBox="0 0 48 48" fill="none" stroke="#e0157f" stroke-width="2"><circle cx="20" cy="20" r="12"/><path d="M29 29l11 11"/><path d="M14 22l4-4 4 3 5-6" stroke="#6b22d8"/></svg>
  <h3>Maecenas fringilla</h3>
  <p>Phasellus ac magna leo. In pulvinar nisl bibendum. Maecenas fringilla ipsum. Phasellus ac magna volutpat bibendum. Phasellus ac magna leo. In pulvinar volutpat bibendum. Maecenas fringilla ipsum.</p>
</div>
<div class="abs method-item" style="left:668px;top:780px">
  <svg width="48" height="48" viewBox="0 0 48 48" fill="none" stroke="#6b22d8" stroke-width="2"><rect x="6" y="8" width="36" height="28" rx="3"/><path d="M12 16h14M12 22h20M12 28h10" stroke="#e0157f"/><path d="M18 42h12"/></svg>
  <h3>Consectetur adipiscing</h3>
  <p>Phasellus ac magna leo. In pulvinar nisl bibendum. Maecenas fringilla ipsum. Phasellus ac magna leo. In pulvinar volutpat bibendum. Phasellus ac magna leo. In pulvinar volutpat.</p>
</div>
<div class="abs method-item" style="left:232px;top:1026px">
  <svg width="48" height="48" viewBox="0 0 48 48" fill="none" stroke="#6b22d8" stroke-width="2"><path d="M6 12h14l4 5h18v22H6z"/><path d="M6 20h36" stroke="#e0157f"/></svg>
  <h3>Paecenas mingilla</h3>
  <p>Phasellus ac magna leo. In pulvinar nisl bibendum. Maecenas fringilla ipsum. Phasellus ac magna volutpat bibendum. Phasellus ac magna leo. In pulvinar.</p>
</div>
<div class="abs method-item" style="left:668px;top:1026px">
  <svg width="48" height="48" viewBox="0 0 48 48" fill="none" stroke="#e0157f" stroke-width="2"><ellipse cx="22" cy="11" rx="13" ry="5"/><path d="M9 11v24c0 3 6 5 13 5M35 11v12"/><path d="M9 23c0 3 6 5 13 5"/><circle cx="35" cy="35" r="7" stroke="#6b22d8"/></svg>
  <h3>Fusce commodo phare</h3>
  <p>Phasellus ac magna leo. In pulvinar nisl bibendum. Maecenas fringilla ipsum. Phasellus ac magna leo. In pulvinar volutpat bibendum. Phasellus ac magna leo.</p>
</div>

<section class="abs offering"></section>
<h2 class="section-title" style="top:1361px">Our Offering</h2>
<div class="abs offer-intro">
  <h3>Maecenas in fringilla ipsum magna leo pulvinar volutpat bibendum.</h3>
  <p>Phasellus ac magna leo. In pulvinar volutpat bibendum. Maecenas fringilla ipsum. Phasellus ac magna volutpat bibendum.</p>
</div>
<div class="abs illustration" style="left:667px;top:1439px;width:333px;height:263px;background:linear-gradient(160deg,#ece4fb,#f7e3ef)" role="img" aria-label="Illustration of a person working at a desk with a laptop"></div>
<div class="abs illustration" style="left:210px;top:2509px;width:333px;height:263px;background:linear-gradient(160deg,#f1e6f8,#fbe4ee)" role="img" aria-label="Illustration of two people working with a laptop and a phone"></div>

<article class="abs offer-card" style="left:182px;top:1586px;height:484px">
  <svg class="blob" width="70" height="90" viewBox="0 0 70 90"><path d="M70 0v90C50 80 40 60 45 40 50 20 30 10 20 0z" fill="url(#bg1)"/><defs><linearGradient id="bg1" x1="0" y1="0" x2="0" y2="1"><stop offset="0" stop-color="#e0157f"/><stop offset="1" stop-color="#6b22d8"/></linearGradient></defs></svg>
  <h4>Fusce Dolorm commodo pharetra</h4><hr>
  <div class="offer-group"><h5>Lorem ipsum dolor consectetur.</h5><ul><li>Curabitur eleifend libero ut sapien</li><li>Fusce commodo pharetra bibendum</li><li>Eget luctus libero at iaculis sapien</li></ul></div>
  <div class="offer-group"><h5>Lorem ipsum dolor consectetur.</h5><ul><li>Curabitur eleifend libero ut sapien</li><li>Fusce commodo pharetra bibendum</li><li>Eget luctus libero at iaculis sapien</li></ul></div>
  <div class="offer-group"><h5>Lorem ipsum dolor consectetur.</h5><ul><li>Curabitur eleifend libero ut sapien</li><li>Fusce commodo pharetra bibendum</li><li>Eget luctus libero at iaculis sapien</li></ul></div>
</article>
<article class="abs offer-card" style="left:611px;top:1755px;height:491px">
  <svg class="blob" width="70" height="90" viewBox="0 0 70 90"><path d="M70 0v90C50 80 40 60 45 40 50 20 30 10 20 0z" fill="url(#bg1)"/></svg>
  <h4>Fusce Dolorm commodo pharetra</h4><hr>
  <div class="offer-group"><h5>Lorem ipsum dolor consectetur.</h5><ul><li>Curabitur eleifend libero ut sapien</li><li>Fusce commodo pharetra bibendum</li><li>Eget luctus libero at iaculis sapien</li></ul></div>
  <div class="offer-group"><h5>Lorem ipsum dolor consectetur.</h5><ul><li>Curabitur eleifend libero ut sapien</li><li>Fusce commodo pharetra bibendum</li><li>Eget luctus libero at iaculis sapien</li></ul></div>
  <div class="offer-group"><h5>Lorem ipsum dolor consectetur.</h5><ul><li>Curabitur eleifend libero ut sapien</li><li>Fusce commodo pharetra bibendum</li><li>Eget luctus libero at iaculis sapien</li></ul></div>
</article>
<article class="abs offer-card" style="left:182px;top:2098px;height:481px">
  <svg class="blob" width="70" height="90" viewBox="0 0 70 90"><path d="M70 0v90C50 80 40 60 45 40 50 20 30 10 20 0z" fill="url(#bg1)"/></svg>
  <h4>Fusce Dolorm commodo pharetra</h4><hr>
  <div class="offer-group"><h5>Lorem ipsum dolor consectetur.</h5><ul><li>Curabitur eleifend libero ut sapien</li><li>Fusce commodo pharetra bibendum</li><li>Eget luctus libero at iaculis sapien</li></ul></div>
  <div class="offer-group"><h5>Lorem ipsum dolor consectetur.</h5><ul><li>Curabitur eleifend libero ut sapien</li><li>Fusce commodo pharetra bibendum</li><li>Eget luctus libero at iaculis sapien</li></ul></div>
</article>
<article class="abs offer-card" style="left:611px;top:2274px;height:491px">
  <svg class="blob" width="70" height="90" viewBox="0 0 70 90"><path d="M70 0v90C50 80 40 60 45 40 50 20 30 10 20 0z" fill="url(#bg1)"/></svg>
  <h4>Fusce Dolorm commodo pharetra</h4><hr>
  <div class="offer-group"><h5>Lorem ipsum dolor consectetur.</h5><ul><li>Curabitur eleifend libero ut sapien</li><li>Fusce commodo pharetra bibendum</li><li>Eget luctus libero at iaculis sapien</li></ul></div>
  <div class="offer-group"><h5>Lorem ipsum dolor consectetur.</h5><ul><li>Curabitur eleifend libero ut sapien</li><li>Fusce commodo pharetra bibendum</li><li>Eget luctus libero at iaculis sapien</li></ul></div>
  <div class="offer-group"><h5>Lorem ipsum dolor consectetur.</h5><ul><li>Curabitur eleifend libero ut sapien</li><li>Fusce commodo pharetra bibendum</li><li>Eget luctus libero at iaculis sapien</li></ul></div>
</article>

<h2 class="section-title" style="top:2916px">Life At Vorelm</h2>
<div class="abs tile clients-tile" style="left:182px;top:2993px;width:267px;height:183px"><small>We Have</small><strong>60+<br>Clients</strong></div>
<div class="abs tile photo" style="left:182px;top:3186px;width:267px;height:176px;background:linear-gradient(135deg,#3b4a66,#1d2434)" role="img" aria-label="Laptop showing analytics dashboards"></div>
<div class="abs tile photo" style="left:467px;top:2993px;width:551px;height:369px;background:linear-gradient(135deg,#4a4038,#2a2622 60%,#6b6560)" role="img" aria-label="Team meeting around a table with laptops"></div>
<div class="abs tile photo" style="left:182px;top:3379px;width:267px;height:376px;background:linear-gradient(160deg,#e9e9ea,#b9bcc2)" role="img" aria-label="Coffee mug beside a laptop on a desk"></div>
<div class="abs tile quote-tile" style="left:467px;top:3379px;width:270px;height:376px">
  <div class="quote-mark">&ldquo;</div>
  <p>&ldquo;Lorem ipsum dolor amet consectetur adipiscing elit. Fusce commodo pharetra volutpat et bibendum. Morbi non. Curabitur eget libero, fringilla in iaculis sapien.&rdquo;</p>
  <div class="who">Lorem ipsum | <span>Pellentus sollicitudin</span></div>
</div>
<div class="abs tile stats-tile" style="left:747px;top:3379px;width:271px;height:183px">
  <div><b>2018</b><span>Lorem ipsum</span></div><div><b>60</b><span>Lorem ipsum</span></div>
  <div><b>8</b><span>Lorem ipsum</span></div><div><b>200</b><span>Lorem ipsum</span></div>
</div>
<div class="abs tile photo" style="left:747px;top:3572px;width:271px;height:183px;background:linear-gradient(135deg,#c8c6cc,#6d6f7a)" role="img" aria-label="Hands typing on a laptop"></div>

<h2 class="section-title" style="top:3817px">Career In Vorelm</h2>
<div class="abs career-photo" role="img" aria-label="Top view of colleagues working together at a desk with laptops and papers"></div>
<div class="abs join-card">
  <h3>Join Vorelm IOT</h3>
  <p>Lorem ipsum dolor sit, consectetur adipiscing elit. Fusce commodo pharetra dolor. Vestibulum mollis massa consequat non. Curabitur eget luctus libero, in iaculis sapien.</p>
  <a href="#">Apply Now</a>
</div>

<h2 class="section-title" style="top:4459px">They Trust Us</h2>
<span class="abs trust-arrow" style="left:172px">&#8249;</span>
<span class="abs trust-arrow" style="left:1012px">&#8250;</span>
<div class="abs trust-row">
  <span class="trust-name"><i></i>PLACEHOLDER</span>
  <span class="trust-name"><i></i>DUMMY</span>
  <span class="trust-name"><i></i>PLACEHOLDER</span>
  <span class="trust-name"><i></i>DUMMY</span>
</div>

<section class="abs contact"></section>
<h2 class="section-title" style="top:4687px">Contact Us</h2>
<div class="abs contact-pill" style="left:218px;width:372px">
  <svg width="22" height="18" viewBox="0 0 22 18"><rect width="22" height="18" rx="3" fill="#6b22d8"/><path d="M2 3l9 7 9-7" stroke="#fff" stroke-width="1.6" fill="none"/></svg>
  hello@vorelm-iot.example
</div>
<div class="abs contact-pill" style="left:611px;width:337px">
  <svg width="20" height="20" viewBox="0 0 24 24"><path d="M6.6 10.8a15 15 0 006.6 6.6l2.2-2.2c.3-.3.7-.4 1-.2 1.1.4 2.3.6 3.6.6.6 0 1 .4 1 1V20c0 .6-.4 1-1 1A17 17 0 013 4c0-.6.4-1 1-1h3.5c.6 0 1 .4 1 1 0 1.3.2 2.5.6 3.6.1.3 0 .7-.2 1z" fill="#6b22d8"/></svg>
  +1 (555) 010 2040
</div>

<footer class="abs site-footer"></footer>
<div class="abs office" style="left:182px"><svg width="14" height="18" viewBox="0 0 14 18"><path d="M7 0a7 7 0 017 7c0 5-7 11-7 11S0 12 0 7a7 7 0 017-7z" fill="#fff"/><circle cx="7" cy="7" r="2.6" fill="#e0157f"/></svg><b>Lorem ipsum</b>48 Harbor Lane<br>Suite 12<br>75000 Sapien</div>
<div class="abs office" style="left:326px"><svg width="14" height="18" viewBox="0 0 14 18"><path d="M7 0a7 7 0 017 7c0 5-7 11-7 11S0 12 0 7a7 7 0 017-7z" fill="#fff"/><circle cx="7" cy="7" r="2.6" fill="#e0157f"/></svg><b>Lorem ipsum</b>48 Harbor Lane<br>Suite 12<br>75000 Sapien</div>
<div class="abs office" style="left:467px"><svg width="14" height="18" viewBox="0 0 14 18"><path d="M7 0a7 7 0 017 7c0 5-7 11-7 11S0 12 0 7a7 7 0 017-7z" fill="#fff"/><circle cx="7" cy="7" r="2.6" fill="#e0157f"/></svg><b>Lorem ipsum</b>48 Harbor Lane<br>Suite 12<br>75000 Sapien</div>
<div class="abs office" style="left:614px"><svg width="14" height="18" viewBox="0 0 14 18"><path d="M7 0a7 7 0 017 7c0 5-7 11-7 11S0 12 0 7a7 7 0 017-7z" fill="#fff"/><circle cx="7" cy="7" r="2.6" fill="#e0157f"/></svg><b>Lorem ipsum</b>48 Harbor Lane<br>Suite 12<br>75000 Sapien</div>
<div class="abs office" style="left:754px"><svg width="14" height="18" viewBox="0 0 14 18"><path d="M7 0a7 7 0 017 7c0 5-7 11-7 11S0 12 0 7a7 7 0 017-7z" fill="#fff"/><circle cx="7" cy="7" r="2.6" fill="#e0157f"/></svg><b>Lorem ipsum</b>48 Harbor Lane<br>Suite 12<br>75000 Sapien</div>
<div class="abs office" style="left:898px"><svg width="14" height="18" viewBox="0 0 14 18"><path d="M7 0a7 7 0 017 7c0 5-7 11-7 11S0 12 0 7a7 7 0 017-7z" fill="#fff"/><circle cx="7" cy="7" r="2.6" fill="#e0157f"/></svg><b>Lorem ipsum</b>48 Harbor Lane<br>Suite 12<br>75000 Sapien</div>
<div class="abs footer-rule"></div>
<nav class="abs footer-nav" style="color:#fff"><span>HOME</span><span>OUR METHODOLOGY</span><span>OUR OFFERING</span><span>CAREERS</span><span>LIFE AT VORELM</span><span>CONTACT</span></nav>
<div class="abs copyright" style="color:#fff">Copyright &copy; 2018 Vorelm IoT. All rights reserved.</div>
<div class="abs socials"><i></i><i></i><i></i><i></i></div>

</body>
</html>
```